Letterhead & Powerpoint Template Design for a Commercial Solar Company

We need these designs for a growing commercial solar company in Austin Texas. We specialize in large-scale/commercial installations. Any assets we design should have the following elements/considerations.
-Authoritative
-Crisp
-Professional
-No Cartoonish Graphics / nothing "cute"
-Should feel more like an engineering firm style than what you typically solar companies
-Not overwhelming

Ultimately are looking for the following in this design
-Letterhead design
-Powerpoint Design (horizontal Pitch deck with a title page design template 3-4 different layouts that we can alternate or use as needed)
-Proposal Design (Vertical layout that has a very professional title page and then just a standard template for interior pages)
-Business Card

Preferred fonts are Inter & Roboto

Dropbox of photo assets to use - https://www.filevaultbox.example/sh/qtrzmenkwpdyhcb/BBBxe472kfLwjRtUpZ9mTvQ8?dl=0

Target Market(s)

C-Suites, Decision Makers, Commercial property owners

Industry/Entity Type

Solar

Font styles to use
Other font styles liked:
• Inter (Primary) Roboto (Secondary)

Colors

Designer to choose colors to be used in the design.

Requirements
Must have
• Authoritative Crisp Styling
Should not have
• cartoonish or bubbly graphics.

```html
<!DOCTYPE html>
<html lang="en">
<head>
<meta charset="utf-8">
<title>Kestrel Solar – Business Card</title>
<link href="https://fonts.googleapis.com/css2?family=Inter:wght@400;500;600;700&display=swap" rel="stylesheet">
<style>
  :root {
    --bg: #e6e6e4;
    --paper: #ffffff;
    --brand-orange: #ef5d2d;
    --ink-grey: #55575a;
    --rule-grey: #a3a5a8;
    --shadow: rgba(0, 0, 0, 0.18);
  }
  * { box-sizing: border-box; margin: 0; padding: 0; }
  html, body {
    width: 1200px;
    height: 802px;
    overflow: hidden;
    background: var(--bg);
    font-family: "Inter", Arial, sans-serif;
  }
  .card-set {
    position: relative;
    width: 1200px;
    height: 802px;
    display: flex;
    align-items: center;
    justify-content: center;
    gap: 60px;
  }
  .card {
    width: 500px;
    height: 286px;
    box-shadow: 0 10px 28px var(--shadow);
    position: relative;
  }
  /* Front */
  .card-front {
    background: var(--paper);
    display: flex;
    align-items: center;
  }
  .front-brand {
    width: 245px;
    display: flex;
    justify-content: center;
  }
  .wordmark {
    font-weight: 600;
    letter-spacing: 0.06em;
    text-transform: uppercase;
    line-height: 1.1;
  }
  .front-brand .wordmark {
    color: var(--ink-grey);
    font-size: 30px;
    text-align: left;
  }
  .divider {
    width: 1px;
    height: 150px;
    background: var(--rule-grey);
  }
  .contact {
    padding-left: 24px;
    color: var(--ink-grey);
    font-size: 12.5px;
    line-height: 1.35;
  }
  .contact-name {
    color: var(--brand-orange);
    font-weight: 600;
    font-size: 15px;
    letter-spacing: 0.01em;
    text-transform: uppercase;
  }
  .contact-role { margin-bottom: 14px; }
  .contact-address { margin-bottom: 14px; }
  .contact-list { list-style: none; }
  .contact-list li {
    display: flex;
    align-items: center;
    gap: 7px;
  }
  .contact-icon { width: 12px; height: 12px; flex: none; }
  /* Back */
  .card-back {
    background: var(--brand-orange);
    display: flex;
    align-items: center;
    justify-content: center;
  }
  .card-back .wordmark {
    color: var(--paper);
    font-size: 44px;
    text-align: center;
  }
</style>
</head>
<body>
  <main class="card-set">
    <section class="card card-front" aria-label="Business card front">
      <div class="front-brand">
        <p class="wordmark">Kestrel<br>Solar</p>
      </div>
      <div class="divider"></div>
      <div class="contact">
        <p class="contact-name">Daniel Reeves</p>
        <p class="contact-role">Manager</p>
        <p class="contact-address">Your Address, City<br>State, Zip 0000</p>
        <ul class="contact-list">
          <li>
            <svg class="contact-icon" viewBox="0 0 12 12" aria-hidden="true">
              <circle cx="6" cy="6" r="6" fill="var(--brand-orange)"/>
              <path d="M3.6 3.4c.3-.3.7-.3.9 0l.6.8c.2.3.1.6-.1.8l-.3.3c.3.7.9 1.3 1.6 1.6l.3-.3c.2-.2.5-.3.8-.1l.8.6c.3.2.3.6 0 .9l-.4.4c-.4.4-1.1.4-1.7.1-1.2-.6-2.3-1.7-2.9-2.9-.3-.6-.3-1.3.1-1.7z" fill="#fff"/>
            </svg>
            <span>123-456-2100</span>
          </li>
          <li>
            <svg class="contact-icon" viewBox="0 0 12 12" aria-hidden="true">
              <rect x="1" y="2.5" width="10" height="7" fill="var(--brand-orange)"/>
              <path d="M1.5 3l4.5 3.4L10.5 3" stroke="#fff" stroke-width="0.9" fill="none"/>
            </svg>
            <span>youremail@mailbox.example</span>
          </li>
          <li>
            <svg class="contact-icon" viewBox="0 0 12 12" aria-hidden="true">
              <circle cx="6" cy="6" r="6" fill="var(--brand-orange)"/>
              <circle cx="6" cy="6" r="3.6" stroke="#fff" stroke-width="0.8" fill="none"/>
              <path d="M2.4 6h7.2M6 2.4c-1.4 1.8-1.4 5.4 0 7.2M6 2.4c1.4 1.8 1.4 5.4 0 7.2" stroke="#fff" stroke-width="0.7" fill="none"/>
            </svg>
            <span>www.yourwebsite.example</span>
          </li>
        </ul>
      </div>
    </section>

    <section class="card card-back" aria-label="Business card back">
      <p class="wordmark">Kestrel<br>Solar</p>
    </section>
  </main>
</body>
</html>
```